Update Old OR create new Website

Current Website is looking a bit old, I did this one a few years back.

Would like a fresh new look, current website sitepress theme is " the Vanta theme" from plumcrate and I just purchased this theme - "bravlo" also from plumcrate, I quite like the look of - http://bravlo.quorvex-skins.com/tech-business/ and if we could get somthing simlar would be great.

current website is at http://www.hle.com.au, have been playing around with the slider that i like.

I have said 5 pages to be designed but really it is just a 5 page website where most pages will look the same.

Any questions please let me know

Target Market(s)

Business

Coding

Coded - Design and coding required

Number of Pages Required

5+ page

Font styles to use
Sans Serif

Colors
33a6d7
0292cd
ffffff
0255a3

Requirements
Must have
• Device compatibility - pc, tablet, phone
Nice to have
• video
Should not have
• vunerabilities. Must also use images that will expire or disappear, ie must be uploaded to site not links to elsewhere.

```html
<!DOCTYPE html>
<html lang="en">
<head>
<meta charset="utf-8">
<title>Halden Technologies</title>
<link href="https://fonts.googleapis.com/css2?family=Open+Sans:wght@400;600;700&display=swap" rel="stylesheet">
<style>
:root{
  --blue:#0292cd;
  --blue-light:#33a6d7;
  --blue-deep:#0255a3;
  --white:#ffffff;
  --green:#2a6a47;
  --green-dark:#245c3e;
  --ink:#333a40;
  --muted:#7a8088;
  --dark:#1b1b1b;
  --paper:#f1f1f1;
}
*{box-sizing:border-box;margin:0;padding:0}
html,body{width:1200px;height:3422px;overflow:hidden}
body{font-family:"Open Sans",Arial,sans-serif;color:var(--white);background:var(--white)}
.topbar{height:22px;background:var(--blue);display:flex;align-items:center;padding-left:270px;gap:14px;font-size:9px}
.topbar .dot{width:9px;height:9px;border-radius:50%;background:var(--white);opacity:.85}
.nav{height:70px;background:var(--white);display:flex;align-items:center;justify-content:space-between;padding:0 262px 0 262px}
.brand{display:flex;align-items:center;gap:8px;color:var(--ink);font-size:20px;font-weight:600}
.brand .mark{width:22px;height:22px;background:var(--blue)}
.menu{display:flex;gap:16px;font-size:10.5px;color:var(--blue)}
.section{position:relative;overflow:hidden}
.section .inner{position:relative;padding-left:121px;width:1060px}
.section h2{font-size:26px;font-weight:400;margin-bottom:6px}
.section p{font-size:12px;line-height:25px}
.down{position:absolute;left:50%;margin-left:-14px;width:28px;height:28px}
.hero{height:570px;background:linear-gradient(100deg,#3f5fd8 0%,#7a4dbf 45%,#c54a95 80%,#d44c7c 100%)}
.hero .inner{padding-top:140px}
.hero .welcome{font-size:10px}
.hero h1{font-size:25px;font-weight:400;margin-bottom:6px}
.btns{display:flex;gap:12px;margin-top:14px}
.btn{border:2px solid var(--white);padding:7px 12px;font-size:11px;text-transform:uppercase}
.btn.solid{background:var(--blue)}
.managed{height:478px;background:linear-gradient(100deg,#106a82 0%,#2a9a6a 45%,#6cc83a 80%,#86d42c 100%)}
.managed .inner{padding-top:130px}
.cloud{height:486px;background:linear-gradient(135deg,#2a2a2a,#3d3d3d 50%,#1f1f1f)}
.cloud .inner{padding-top:125px}
.servers{height:472px;background:radial-gradient(circle at 80% 40%,#26407a 0%,#111a3c 45%,#0a0f24 100%)}
.servers .inner{padding-top:138px}
.web{height:320px;background:var(--green);text-align:center}
.web h3,.apps h3,.internet h3,.contact h3{font-size:17px;font-weight:700;letter-spacing:.5px}
.web h3{padding-top:70px;margin-bottom:24px}
.tags{display:grid;grid-template-columns:repeat(3,190px);gap:22px 52px;justify-content:center}
.tag{background:var(--blue);border:2px solid var(--white);height:30px;font-size:11px;display:flex;align-items:center;justify-content:center;gap:5px}
.apps{height:330px;background:var(--paper);color:var(--ink);text-align:center}
.apps h3{padding-top:62px;margin-bottom:28px}
.steps{display:flex;justify-content:center;gap:60px}
.step{width:84px;font-size:14px;line-height:15px;color:#555}
.step svg{width:56px;height:56px;margin-bottom:10px}
.internet{height:304px;background:var(--green)}
.internet h3{text-align:center;padding-top:72px;margin-bottom:20px}
.internet .copy{width:700px;margin-left:261px;font-size:11.5px;line-height:22px}
.internet .copy p{margin-bottom:10px}
.contact{height:370px;background:var(--dark)}
.portrait{position:absolute;left:296px;top:0;width:274px;height:370px;background:radial-gradient(ellipse at 50% 40%,#8a6a56 0%,#4d4a4a 45%,#1b1b1b 75%)}
.form{position:absolute;left:623px;top:20px;width:324px}
.form h3{text-align:center;margin-bottom:18px}
.row{display:flex;gap:14px}
.field{border:1px solid #cfcfcf;height:32px;font-size:9px;padding:9px 6px;flex:1;margin-bottom:10px}
.field.area{height:96px}
.submitrow{display:flex;justify-content:flex-end;align-items:center;gap:10px;font-size:9px;color:#888;margin-top:4px}
.captcha{width:30px;height:30px;border:1px solid #cfcfcf}
.submit{border:2px solid var(--blue);color:var(--blue);padding:6px 14px;font-size:12px}
.social{position:absolute;left:836px;top:346px;display:flex;gap:18px}
.social span{width:12px;height:12px;border-radius:50%;background:#888}
.band{position:absolute;left:0;width:1200px}
</style>
</head>
<body>
<div class="topbar"><span>1300 555 014</span><span>info@hle.com.au</span><span class="dot"></span><span class="dot"></span><span class="dot"></span><span class="dot"></span></div>
<header class="nav">
  <div class="brand"><span class="mark"></span><span>Halden Technologies</span></div>
  <nav class="menu"><span>Home</span><span>Managed IT</span><span>Private</span><span>Servers</span><span>Web</span><span>Apps</span><span>Internet</span><span>Contact Us</span></nav>
</header>

<section class="section hero" role="img" aria-label="Office desk photo under a blue to pink gradient with a network line pattern">
  <div class="inner">
    <div class="welcome">Welcome to</div>
    <h1>Halden Technologies For Website Des</h1>
    <p>What would it take for your information systems to actually improve the performance of your organisation?<br>
    Through Halden Technologies, companies outsource all the expertise they need to secure their systems and optimise the output of their people and IT resources – without the expense of maintaining large internal IT departments.<br>
    With a decade of experience, Halden Technologies understands the challenges faced by SMEs. So when we design and build networks, support solutions, hardware and software there's room for growth, change and mobility.<br>
    Halden Technologies staff are not just short-term problem solvers – they are advanced systems designers and proactive thinkers who work closely with clients on issue detection and prevention. And, when problems do arise Halden Technologies literally does whatever it takes to get clients back on track.<br>
    It's this attitude that means Halden Technologies enjoys long-term relationships with its clients.</p>
    <div class="btns"><span class="btn solid">Solutions</span><span class="btn">Contact Us</span></div>
  </div>
  <svg class="down" style="top:520px" viewBox="0 0 28 28"><circle cx="14" cy="14" r="12" fill="none" stroke="#fff" stroke-width="2"/><path d="M8 12l6 6 6-6" fill="none" stroke="#fff" stroke-width="2"/></svg>
</section>

<section class="section managed">
  <div class="inner">
    <h2>Managed IT</h2>
    <p>Clients in all industries outsource Halden Technologies for Onsite Server Maintenance Plans and Managed IT Services.<br>
    This function is critical to business because software, hardware and external threats to systems are always changing. Servers can physically wear out while new viruses and spyware are constantly under development.<br>
    Clients choose Halden Technologies because Halden's core focus is on anticipating and preventing issues before they turn in to problems. These clients then get the best performance from their systems and people and maintain data security – without the expense of an internal IT department.<br>
    Halden Technologies Onsite Server Maintenance Plans are custom designed to exactly suit the client's industry and business model. Service agreement levels range from just four hours a month to full time on site support.</p>
  </div>
  <svg class="down" style="top:430px" viewBox="0 0 28 28"><circle cx="14" cy="14" r="12" fill="none" stroke="#fff" stroke-width="2"/><path d="M8 12l6 6 6-6" fill="none" stroke="#fff" stroke-width="2"/></svg>
</section>

<section class="section cloud" role="img" aria-label="Dim photo of a computer workstation">
  <div class="inner">
    <h2>Private Cloud</h2>
    <p>Halden Technologies provides the design, support and maintenance for quality I.T Systems for clients to thrive, change and grow.<br>
    Halden offers Private Cloud solutions, the most secure version of "the Cloud" it is the premium IT system and we guarantee that you owing your physical infrastructure will be the best IT decision you make for your business. Clients choose Halden Technologies for hardware and service because it is more efficient to have their entire IT infrastructure managed by one supplier as part of a complete package; there's less to co-ordinate, fewer relationships to manage and less to go wrong.<br>
    What's more, the Halden Staff are super familiar with the intricacies of these systems and can provide faster responses if there's an issue to deal with.</p>
  </div>
  <svg class="down" style="top:440px;opacity:.4" viewBox="0 0 28 28"><circle cx="14" cy="14" r="12" fill="none" stroke="#fff" stroke-width="2"/><path d="M8 12l6 6 6-6" fill="none" stroke="#fff" stroke-width="2"/></svg>
</section>

<section class="section servers" role="img" aria-label="Dark blue abstract network of glowing points and lines">
  <div class="inner">
    <h2>Servers</h2>
    <p>Halden Technologies System Design solutions give clients whatever they need to pursue their business objectives. Halden recommendations are always developed collaboratively with clients and they allow for future growth and change.<br>
    From networking a brand new building, to a system upgrade, the Halden team provide systems design and installation services that encompass all elements from server specification, cabling and PCs to boardroom data projectors.<br>
    Halden team members take great pride in their depth of understanding of their client's industries and business models. This knowledge provides them with insight that means their designs deliver immediate improvements to users and are cost effective in the long-term.<br>
    Halden system design and installation expertise ensures clients have the best technology to work with.</p>
  </div>
  <svg class="band" style="top:420px" width="1200" height="52" viewBox="0 0 1200 52"><polygon points="0,52 1200,12 1200,52" fill="var(--green)"/><polygon points="0,52 1200,0 1200,12 0,52" fill="var(--blue)"/></svg>
  <svg class="down" style="top:430px" viewBox="0 0 28 28"><circle cx="14" cy="14" r="12" fill="none" stroke="#fff" stroke-width="2"/><path d="M8 12l6 6 6-6" fill="none" stroke="#fff" stroke-width="2"/></svg>
</section>

<section class="section web">
  <h3>WEB</h3>
  <div class="tags">
    <span class="tag">✓ Website Design</span><span class="tag">✓ Digital Strategy</span><span class="tag">✓ CMS</span>
    <span class="tag">✓ Web Marketing</span><span class="tag">✓ SEO</span><span class="tag">✓ Pay Per Click</span>
    <span class="tag">✓ Remarketing</span><span class="tag">✓ Copywriting</span><span class="tag">✓ SMM</span>
  </div>
  <svg class="band" style="top:268px" width="1200" height="52" viewBox="0 0 1200 52"><polygon points="0,52 1200,0 1200,18 0,52" fill="var(--blue)"/><polygon points="0,52 1200,18 1200,52" fill="var(--paper)"/></svg>
</section>

<section class="section apps">
  <h3>APPS</h3>
  <div class="steps">
    <div class="step"><svg viewBox="0 0 56 56" fill="none" stroke="#333" stroke-width="2"><ellipse cx="28" cy="28" rx="24" ry="9"/><ellipse cx="28" cy="28" rx="24" ry="9" transform="rotate(60 28 28)"/><ellipse cx="28" cy="28" rx="24" ry="9" transform="rotate(120 28 28)"/><circle cx="28" cy="28" r="3" fill="#333"/></svg>Discovery &amp; Strategy</div>
    <div class="step"><svg viewBox="0 0 56 56" fill="none" stroke="#333" stroke-width="2"><path d="M8 14h40M8 28h40M8 42h40"/><rect x="30" y="10" width="6" height="8" fill="#f1f1f1"/><rect x="16" y="24" width="6" height="8" fill="#f1f1f1"/><rect x="34" y="38" width="6" height="8" fill="#f1f1f1"/></svg>User Experience Design</div>
    <div class="step"><svg viewBox="0 0 56 56" fill="none" stroke="#333" stroke-width="2"><rect x="16" y="4" width="24" height="48" rx="4"/><path d="M16 12h24M16 42h24"/><circle cx="28" cy="47" r="2"/></svg>Mobile App Development</div>
    <div class="step"><svg viewBox="0 0 56 56" fill="none" stroke="#333" stroke-width="2"><path d="M10 18h10a5 5 0 1 1 10 0h10v10a5 5 0 1 1 0 10v10H10V38a5 5 0 1 0 0-10z"/></svg>Business Application Development</div>
    <div class="step"><svg viewBox="0 0 56 56" fill="none" stroke="#333" stroke-width="2"><path d="M14 40a9 9 0 0 1 0-18 13 13 0 0 1 25-3 10 10 0 0 1 3 21z"/><path d="M28 44V28M22 34l6-6 6 6"/></svg>Testing &amp; Deployment</div>
  </div>
  <svg class="band" style="top:278px" width="1200" height="52" viewBox="0 0 1200 52"><polygon points="0,52 1200,0 1200,16 0,52" fill="var(--blue)"/><polygon points="0,52 1200,16 1200,52" fill="var(--green)"/></svg>
</section>

<section class="section internet">
  <h3>Internet Solutions</h3>
  <div class="copy">
    <p>Halden Technologies is a Corvane, Optilink and Tessnet partner. We have access to a different Tier of support so can get things fixed for you faster when there is a problem.</p>
    <p>Having access to the leading providers of Internet in Australia we can determine not only who will give you the fastest connection speeds with you Internet, Data, Mobile and corporate phone plans but who is going to give you the best value for money.</p>
    <p>Call us now on 1300 555 014</p>
  </div>
</section>

<section class="section contact">
  <div class="portrait" role="img" aria-label="Photo of a smiling support agent wearing a headset"></div>
  <div class="form">
    <h3>CONTACT US</h3>
    <div class="row"><div class="field">Name</div><div class="field">Email Address</div></div>
    <div class="field">Subject</div>
    <div class="field area">Message</div>
    <div class="submitrow"><span>5 + 11 =</span><span class="captcha"></span><span class="submit">Submit</span></div>
  </div>
  <div class="social" aria-label="Social links"><span></span><span></span><span></span><span></span></div>
</section>
</body>
</html>
```